Business Card Design Project

This is the first time we use our new logo. We need a business card that we can use both on our institutional corporate relationships and also that works for our staff that deals with consumers directly.

VELUNDA is a new company dedicated to empower consumers and to provide them with the best choices for specialized health care using the latest telemedicine technology (medicine at a distance via videoconference).

We want to print this cards in high quality materials and process. We will like designs that allow us to use UV spot varnish and other techniques that will differentiate us.

We are including Two different versions of Color logos. In addition we are including white over black background logos. Those can be used replacing the black for a color.

Please note this is the first time we will be creating any corporate materials with our new logo and colors.

Target Market(s)

34+ consumers of medium high and high socioeconomic levels.

Industry/Entity Type

Health

Requirements
Must have
• Our logo on its original colors
Should not have
• Any other graphical element or design that is not our logo

```html
<!DOCTYPE html>
<html lang="en">
<head>
<meta charset="utf-8">
<title>VELUNDA Business Card</title>
<link href="https://fonts.googleapis.com/css2?family=Jost:wght@600&family=Open+Sans:wght@400;600&display=swap" rel="stylesheet">
<style>
  :root {
    --backdrop: #e6e7e9;
    --card-dark: #434346;
    --card-light: #ffffff;
    --brand-blue: #1f76bb;
    --sky-blue: #5ab4e0;
    --navy: #1d4f7a;
    --ink: #333333;
    --white: #ffffff;
  }
  html, body {
    margin: 0;
    padding: 0;
    overflow: hidden;
  }
  body {
    width: 1200px;
    height: 513px;
    background: var(--backdrop);
    position: relative;
  }
  .card {
    position: absolute;
    top: 126px;
    width: 459px;
    height: 262px;
    border-radius: 26px;
    overflow: hidden;
    box-shadow: 0 6px 18px rgba(0,0,0,0.18);
  }
  .card svg { display: block; }
  .card--front { left: 134px; background: var(--card-dark); }
  .card--back { left: 608px; background: var(--card-light); }
  .wordmark {
    font-family: "Jost", "Futura", sans-serif;
    font-weight: 600;
    letter-spacing: 2px;
  }
  .wordmark--light { fill: var(--white); }
  .wordmark--dark { fill: var(--navy); }
  .person-name {
    font-family: "Open Sans", sans-serif;
    font-size: 15px;
    fill: var(--ink);
  }
  .person-role {
    font-family: "Open Sans", sans-serif;
    font-weight: 600;
    font-size: 11px;
    fill: var(--brand-blue);
  }
  .contact-line {
    font-family: "Open Sans", sans-serif;
    font-size: 12.5px;
    fill: var(--ink);
  }
  .icon { fill: var(--brand-blue); }
</style>
</head>
<body>

<div class="card card--front">
  <svg width="459" height="262" viewBox="0 0 525 300" preserveAspectRatio="none">
    <path d="M0 272 Q262 200 525 272 L525 300 L0 300 Z" fill="var(--white)"/>
    <path d="M0 286 Q262 216 525 286 L525 300 L0 300 Z" fill="var(--brand-blue)"/>
    <circle class="brand-dot" cx="168" cy="148" r="12" fill="var(--white)"/>
    <text class="wordmark wordmark--light" x="192" y="164" font-size="40">VELUNDA</text>
  </svg>
</div>

<div class="card card--back">
  <svg width="459" height="262" viewBox="0 0 525 300" preserveAspectRatio="none">
    <path d="M0 280 Q262 200 525 280 L525 300 L0 300 Z" fill="var(--sky-blue)"/>
    <path d="M0 294 Q262 218 525 294 L525 300 L0 300 Z" fill="var(--brand-blue)"/>

    <circle class="brand-dot" cx="128" cy="150" r="11" fill="var(--navy)"/>
    <text class="wordmark wordmark--dark" x="128" y="200" font-size="34" text-anchor="middle">VELUNDA</text>

    <line x1="279" y1="135" x2="279" y2="201" stroke="var(--brand-blue)" stroke-width="2"/>

    <text class="person-name" x="301" y="95">Mara Solden</text>
    <text class="person-role" x="301" y="113">CEO</text>

    <g class="contact-list">
      <rect class="icon" x="301" y="132" width="7" height="11" rx="1.5"/>
      <text class="contact-line" x="321" y="143">(555) 014-2290</text>

      <rect class="icon" x="299" y="154" width="12" height="7" rx="1"/>
      <rect class="icon" x="302" y="150" width="6" height="4"/>
      <text class="contact-line" x="321" y="161">(555) 014-2291</text>

      <rect class="icon" x="299" y="168" width="13" height="9" rx="1"/>
      <path d="M299 168 L305.5 174 L312 168" fill="none" stroke="var(--white)" stroke-width="1.2"/>
      <text class="contact-line" x="321" y="178">contact@velunda.com</text>

      <circle class="icon" cx="305.5" cy="191" r="6"/>
      <path d="M299.5 191 H311.5 M305.5 185 V197" stroke="var(--white)" stroke-width="1"/>
      <ellipse cx="305.5" cy="191" rx="2.6" ry="6" fill="none" stroke="var(--white)" stroke-width="1"/>
      <text class="contact-line" x="321" y="196">www.velunda.com</text>
    </g>
  </svg>
</div>

</body>
</html>
```